KT-Systems advertising flag and billboard design

I need a design for advertising flag and a design for billboard.
Information can be obtained from https://kt-sytronik.de.
Updates
Target Market(s)
IT service for companies
Requirements
Must have
- Logo, contact information and services

```html
<!DOCTYPE html>
<html lang="en">
<head>
<meta charset="utf-8">
<title>KT-Systems roll-up banners</title>
<link rel="stylesheet" href="https://fonts.googleapis.com/css2?family=Archivo:wght@700&family=Open+Sans:wght@600;700&display=swap">
<style>
  :root {
    --charcoal: #434444;
    --brand-blue: #5777bd;
    --paper: #ffffff;
    --ink: #1e1e1e;
    --backdrop: #e4e5e7;
    --photo-light: #dfe6ee;
    --photo-mid: #b9c6d6;
    --photo-warm: #e8d2c2;
  }
  * { margin: 0; padding: 0; box-sizing: border-box; }
  html, body { width: 1200px; height: 846px; overflow: hidden; background: var(--backdrop); }
  .canvas { position: relative; width: 1200px; height: 846px; }
  .banner { position: absolute; top: 155px; width: 276px; height: 500px; display: block; }
  .banner--services { left: 267px; }
  .banner--team { left: 694px; }
  .brand-name { font-family: "Open Sans", sans-serif; font-weight: 700; fill: var(--paper); letter-spacing: 1px; }
  .brand-url { font-family: "Archivo", sans-serif; font-weight: 700; fill: var(--paper); }
  .headline { font-family: "Open Sans", sans-serif; font-weight: 700; fill: var(--paper); }
  .headline .accent { fill: var(--brand-blue); }
  .service-label { font-family: "Archivo", sans-serif; font-weight: 700; font-size: 10.5px; fill: var(--ink); }
  .node { fill: var(--paper); stroke: var(--brand-blue); stroke-width: 1.6; }
  .link { stroke: var(--brand-blue); stroke-width: 2.2; }
  .icon { fill: none; stroke: var(--ink); stroke-width: 1.4; stroke-linecap: round; stroke-linejoin: round; }
</style>
</head>
<body>
<main class="canvas">

  <svg class="banner banner--services" viewBox="0 0 276 500" xmlns="http://www.w3.org/2000/svg">
    <rect width="276" height="500" fill="var(--paper)"/>
    <polygon points="0,0 276,0 276,190 141,217 0,242" fill="var(--charcoal)"/>
    <polygon points="141,217 276,190 276,265" fill="var(--brand-blue)"/>

    <text class="brand-name" x="138" y="35" font-size="18" text-anchor="middle">KT-SYSTEMS</text>
    <text class="brand-url" x="138" y="58" font-size="10.5" text-anchor="middle">https://kt-sytronik.de</text>

    <text class="headline" x="138" y="112" font-size="36" text-anchor="middle">Your partner</text>
    <text class="headline" x="138" y="161" font-size="36" text-anchor="middle">for <tspan class="accent">IT-Services</tspan></text>

    <g class="service-map">
      <line class="link" x1="74" y1="290" x2="114" y2="271"/>
      <line class="link" x1="165" y1="271" x2="204" y2="290"/>
      <line class="link" x1="51" y1="338" x2="51" y2="360"/>
      <line class="link" x1="228" y1="338" x2="228" y2="360"/>
      <line class="link" x1="95" y1="412" x2="115" y2="422"/>
      <line class="link" x1="165" y1="422" x2="188" y2="412"/>

      <rect x="90" y="305" width="100" height="82" fill="var(--charcoal)" role="img" aria-label="Illustration of an IT technician working on a laptop"/>

      <circle class="node" cx="140" cy="260" r="16"/>
      <g class="icon"><rect x="134" y="253" width="13" height="9"/><line x1="140" y1="262" x2="140" y2="266"/><line x1="136" y1="266" x2="144" y2="266"/></g>
      <text class="service-label" x="140" y="239" text-anchor="middle">PC Repair</text>

      <circle class="node" cx="51" cy="303" r="16"/>
      <g class="icon"><rect x="45" y="297" width="12" height="8"/><line x1="42" y1="308" x2="60" y2="308"/></g>
      <text class="service-label" x="51" y="329" text-anchor="middle">Laptop Repair</text>

      <circle class="node" cx="228" cy="303" r="16"/>
      <g class="icon"><circle cx="228" cy="303" r="7"/><polyline points="224,303 227,306 233,299"/></g>
      <text class="service-label" x="228" y="327" text-anchor="middle">System Check</text>

      <circle class="node" cx="51" cy="389" r="16"/>
      <g class="icon"><path d="M51 381 l7 3 v5 c0 5 -4 7 -7 8 c-3 -1 -7 -3 -7 -8 v-5 z"/></g>
      <text class="service-label" x="51" y="414" text-anchor="middle">Malware and</text>
      <text class="service-label" x="51" y="426" text-anchor="middle">Virus Removing</text>

      <circle class="node" cx="228" cy="389" r="16"/>
      <g class="icon"><path d="M228 381 l7 3 v5 c0 5 -4 7 -7 8 c-3 -1 -7 -3 -7 -8 v-5 z"/><polyline points="225,389 227,391 231,387"/></g>
      <text class="service-label" x="228" y="416" text-anchor="middle">Data Backup</text>
      <text class="service-label" x="228" y="428" text-anchor="middle">&amp; Recovery</text>

      <circle class="node" cx="140" cy="431" r="16"/>
      <g class="icon"><rect x="135" y="423" width="10" height="4"/><rect x="135" y="428" width="10" height="4"/><rect x="135" y="433" width="10" height="4"/></g>
      <text class="service-label" x="140" y="464" text-anchor="middle">Network / Servers</text>
    </g>
  </svg>

  <svg class="banner banner--team" viewBox="0 0 276 500" xmlns="http://www.w3.org/2000/svg">
    <defs>
      <linearGradient id="team-photo-tone" x1="0" y1="0" x2="1" y2="1">
        <stop offset="0" stop-color="var(--photo-mid)"/>
        <stop offset="0.45" stop-color="var(--photo-light)"/>
        <stop offset="0.75" stop-color="var(--photo-warm)"/>
        <stop offset="1" stop-color="var(--photo-light)"/>
      </linearGradient>
    </defs>
    <rect width="276" height="84" fill="var(--charcoal)"/>
    <text class="brand-name" x="138" y="40" font-size="20" text-anchor="middle">KT-SYSTEMS</text>
    <text class="brand-url" x="138" y="65" font-size="15" text-anchor="middle" style="font-family:'Open Sans',sans-serif;font-weight:600">https://kt-sytronik.de</text>

    <rect y="84" width="276" height="154" fill="var(--brand-blue)"/>
    <text class="headline" x="138" y="144" font-size="36" text-anchor="middle">Your partner</text>
    <text class="headline" x="138" y="194" font-size="36" text-anchor="middle">for IT-Services</text>

    <rect y="238" width="276" height="262" fill="url(#team-photo-tone)" role="img" aria-label="Photo of two smiling colleagues looking at a laptop in a bright office"/>
  </svg>

</main>
</body>
</html>
```